White Rum brand needs bottle label

Looking for a label that will stand out on a shelf and feel like an instant classic. Corvane is a premium Caribbean blended white rum that was crafted as an escape from day-to-day stress and is all about making each day feel as though it's a vacation day. It was named after two local beaches and surf breaks both of which are party towns. I'd like the label to feel modern, sleek, and casual, while still feeling very slightly upscale and have a few subtle hints of it's tropical origin. Corvane should look suitable to drink in variety of situations such as a casual drink at the beach or a pool, a cocktail after a long day of work, or a night out at a bar or club. Please incorporate the logo somewhere in the label, whether that's just the mermaid or the entire design I'll leave that up to the designer. Whatever it is, it should have a look that is scalable and feels appropriate to consume in many settings while remembering it's Carribean and beach roots.

Target Market(s)

The target market is fairly broad. Target consumers are between 21-55, leaning slightly more towards the masculine crowd, full-time workers that enjoy drinking regularly.

Font styles to use
Serif
Sans Serif

Requirements
Must have
• Must have at least the mermaid part of the logo incorporated within the label.
Nice to have
• I'd like a bottle with a synthetic cork, that has a strap sealer over the top and a bottle shaped similar to Valdoro Tequila. Colors are designer's choice. Subtle floral or tropical notes (not too much) mixed into a fairly sleek and modern design.

```html
<!DOCTYPE html>
<html lang="en">
<head>
<meta charset="utf-8">
<title>Corvane White Rum — Label Set</title>
<link href="https://fonts.googleapis.com/css2?family=Oswald:wght@400;500;700&family=Montserrat:wght@700;800&family=Barlow+Condensed:wght@600;700&display=swap" rel="stylesheet">
<style>
  :root {
    --cyan: #17bfd9;
    --cyan-mid: #6fd0e3;
    --cyan-soft: #8fdcea;
    --cyan-light: #bfeaf3;
    --cyan-pale: #d4f2f7;
    --ink: #161616;
    --seal-red: #e0342f;
    --rim-grey: #c9c9c9;
    --paper: #ffffff;
    --page: #ffffff;
  }
  * { margin: 0; padding: 0; box-sizing: border-box; }
  html, body {
    width: 1200px;
    height: 1028px;
    overflow: hidden;
    background: var(--page);
  }
  .label-set {
    position: relative;
    width: 1200px;
    height: 1028px;
  }
  .neck-strap {
    position: absolute;
    left: 136px;
    top: 90px;
    width: 187px;
    height: 847px;
  }
  .front-label {
    position: absolute;
    left: 473px;
    top: 84px;
    width: 590px;
    height: 860px;
  }
  .strap-small {
    font-family: "Barlow Condensed", sans-serif;
    font-weight: 600;
    font-size: 13px;
    letter-spacing: 3px;
    fill: var(--paper);
  }
  .strap-name {
    font-family: "Barlow Condensed", sans-serif;
    font-weight: 700;
    font-size: 40px;
    letter-spacing: 7px;
    fill: var(--paper);
  }
  .strap-seal-name {
    font-family: "Oswald", sans-serif;
    font-weight: 500;
    font-size: 24px;
    letter-spacing: 2px;
    fill: var(--paper);
  }
  .arc-words {
    font-family: "Montserrat", sans-serif;
    font-weight: 800;
    font-size: 22px;
    letter-spacing: 9px;
    fill: var(--ink);
  }
  .brand-name {
    font-family: "Oswald", sans-serif;
    font-weight: 700;
    font-size: 132px;
    letter-spacing: 2px;
    fill: var(--ink);
    stroke: var(--paper);
    stroke-width: 3px;
    paint-order: stroke;
  }
  .product-type {
    font-family: "Oswald", sans-serif;
    font-weight: 500;
    font-size: 68px;
    fill: var(--cyan);
    stroke: var(--paper);
    stroke-width: 6px;
    paint-order: stroke;
  }
  .seal-name {
    font-family: "Oswald", sans-serif;
    font-weight: 500;
    font-size: 22px;
    letter-spacing: 1px;
    fill: var(--seal-red);
  }
  .volume-line {
    font-family: "Oswald", sans-serif;
    font-weight: 400;
    font-size: 25px;
    fill: var(--ink);
  }
</style>
</head>
<body>
<main class="label-set">

  <svg class="neck-strap" viewBox="0 0 187 847" aria-label="Neck strap seal">
    <defs>
      <linearGradient id="leaf-tone" x1="0" y1="0" x2="0" y2="1">
        <stop offset="0" stop-color="var(--cyan)"/>
        <stop offset="1" stop-color="var(--cyan-soft)"/>
      </linearGradient>
    </defs>
    <path class="strap-band" d="M25 120 H162 V797 L25 847 Z" fill="var(--cyan)"/>
    <circle class="strap-disc" cx="93.5" cy="93.5" r="93" fill="var(--cyan)"/>
    <circle class="strap-disc-ring" cx="93.5" cy="93.5" r="76" fill="none" stroke="var(--cyan-pale)" stroke-width="1.5" stroke-dasharray="2 3"/>
    <text class="strap-seal-name" x="93.5" y="102" text-anchor="middle">CORVANE</text>

    <line x1="66" y1="192" x2="66" y2="572" stroke="var(--paper)" stroke-width="1.5" stroke-dasharray="3 3"/>
    <line x1="121" y1="192" x2="121" y2="572" stroke="var(--paper)" stroke-width="1.5" stroke-dasharray="3 3"/>

    <text class="strap-small" transform="translate(49 374) rotate(-90)" text-anchor="middle" dominant-baseline="central">PREMIUM CARIBBEAN</text>
    <text class="strap-name" transform="translate(93.5 374) rotate(-90)" text-anchor="middle" dominant-baseline="central">CORVANE</text>
    <text class="strap-small" transform="translate(140 374) rotate(-90)" text-anchor="middle" dominant-baseline="central">BLENDED WHITE RUM</text>

    <path class="strap-foliage" role="img" aria-label="Tropical leaf pattern" d="M25 600 H162 V797 L25 847 Z" fill="url(#leaf-tone)" opacity="0.7"/>
  </svg>

  <svg class="front-label" viewBox="0 0 590 860" aria-label="Front label">
    <defs>
      <linearGradient id="mermaid-tone" x1="0" y1="0" x2="0.3" y2="1">
        <stop offset="0" stop-color="var(--cyan-soft)"/>
        <stop offset="0.55" stop-color="var(--cyan-mid)"/>
        <stop offset="1" stop-color="var(--cyan-light)"/>
      </linearGradient>
      <path id="label-arc" d="M52 430 A243 373 0 0 1 538 430"/>
    </defs>

    <ellipse class="label-rim" cx="295" cy="430" rx="291" ry="426" fill="var(--paper)" stroke="var(--rim-grey)" stroke-width="6"/>
    <ellipse class="label-inner-rule" cx="295" cy="430" rx="276" ry="410" fill="none" stroke="var(--rim-grey)" stroke-width="2.5"/>

    <text class="arc-words">
      <textPath href="#label-arc" startOffset="50%" text-anchor="middle">• PREMIUM • CARIBBEAN • BLENDED •</textPath>
    </text>

    <rect class="mermaid-illustration" role="img" aria-label="Stippled cyan mermaid holding a rum jug, tail curling below" x="150" y="135" width="330" height="530" rx="150" fill="url(#mermaid-tone)"/>

    <text class="brand-name" x="295" y="500" text-anchor="middle">CORVANE</text>
    <text class="product-type" x="540" y="585" text-anchor="end" transform="rotate(-4 540 585)">WHITE RUM</text>

    <circle class="seal-ring" cx="140" cy="682" r="60" fill="var(--paper)" stroke="var(--seal-red)" stroke-width="2"/>
    <text class="seal-name" x="140" y="690" text-anchor="middle">CORVANE</text>

    <line x1="188" y1="724" x2="400" y2="724" stroke="var(--ink)" stroke-width="1.5"/>
    <text class="volume-line" x="295" y="757" text-anchor="middle">700 ML  |  37% VOL</text>
    <line x1="188" y1="770" x2="400" y2="770" stroke="var(--ink)" stroke-width="1.5"/>
  </svg>

</main>
</body>
</html>
```